Zielgruppe
Wir machen Softwareentwicklung. Die Zielgruppe sind Geschäftsführer und Leute aus Leitungspositionen aus dem IT Bereich.
Aufgabenstellung
Ich fände es toll, zwei Designs zu haben. Eine etwas seriösere für Geschäftstermine und eine lockere/verspielte für Meetups und Termine an denen ich eher Angestellte suche.
Bitte auch eine Variante mit QR Code.
Die Angaben auf der Visitenkarte sind:
Max Mustermann (Name des Angestellten)
Position
Adresse-Strasse
Adresse-Postleitzahl und Ort
Telefonnummer (bitte keine Fax-Nummer)
Emailadresse
Webadresse

```html
<!DOCTYPE html>
<html lang="de">
<head>
<meta charset="utf-8">
<title>Codewerk Lindner – Visitenkarte</title>
<link href="https://fonts.googleapis.com/css2?family=Barlow:wght@400;500;600&display=swap" rel="stylesheet">
<style>
  :root {
    --bg: #e6e7ea;
    --card: #ffffff;
    --brand: #1f86c4;
    --brand-deep: #14597f;
    --ink: #222528;
    --ink-soft: #3a3e42;
  }
  * { box-sizing: border-box; margin: 0; padding: 0; }
  html, body { width: 1200px; height: 857px; overflow: hidden; }
  body {
    background: var(--bg);
    font-family: "Barlow", Arial, sans-serif;
    color: var(--ink);
    position: relative;
  }
  .card {
    position: absolute;
    top: 270px;
    width: 500px;
    height: 323px;
    background: var(--card);
    overflow: hidden;
    box-shadow: 0 6px 18px rgba(0,0,0,.12);
  }
  .card--front { left: 70px; }
  .card--back { left: 630px; }

  /* Front */
  .brand {
    position: absolute;
    top: 34px;
    left: 150px;
    display: flex;
    align-items: center;
    gap: 12px;
  }
  .brand__square {
    width: 34px;
    height: 34px;
    background: var(--brand);
    border-radius: 6px;
  }
  .brand__name {
    font-weight: 600;
    font-size: 26px;
    letter-spacing: 1px;
    text-transform: uppercase;
    color: var(--brand);
  }
  .front-decoration {
    position: absolute;
    left: 50px;
    top: 120px;
    width: 200px;
    height: 203px;
    border-radius: 14px 14px 0 0;
    background: linear-gradient(160deg, #cfe5f3 0%, #8cc0e0 100%);
  }

  /* Back */
  .back-decoration {
    position: absolute;
    left: 0;
    top: 0;
    width: 160px;
    height: 62px;
    border-radius: 0 0 14px 0;
    background: linear-gradient(160deg, #cfe5f3 0%, #8cc0e0 100%);
  }
  .person {
    position: absolute;
    left: 34px;
    top: 150px;
  }
  .person__name {
    font-weight: 600;
    font-size: 15px;
    letter-spacing: .4px;
  }
  .person__role {
    font-size: 12px;
    color: var(--ink-soft);
    margin-top: 2px;
  }
  .person__address {
    font-size: 12px;
    line-height: 1.35;
    color: var(--ink-soft);
    margin-top: 14px;
  }
  .contact {
    position: absolute;
    left: 300px;
    top: 138px;
    list-style: none;
    font-size: 12px;
    color: var(--ink-soft);
  }
  .contact li {
    display: flex;
    align-items: center;
    gap: 7px;
    margin-bottom: 5px;
  }
  .contact svg { width: 12px; height: 12px; fill: var(--ink); flex: none; }
</style>
</head>
<body>

  <section class="card card--front">
    <div class="brand">
      <span class="brand__square"></span>
      <span class="brand__name">Codewerk Lindner</span>
    </div>
    <div class="front-decoration" role="img" aria-label="Große dekorative Fläche für das Firmenzeichen"></div>
  </section>

  <section class="card card--back">
    <div class="back-decoration" role="img" aria-label="Angeschnittene dekorative Fläche für das Firmenzeichen"></div>

    <div class="person">
      <p class="person__name">Max Mustermann</p>
      <p class="person__role">Position</p>
      <p class="person__address">Musterstraße 12<br>21345 Musterstadt</p>
    </div>

    <ul class="contact">
      <li>
        <svg viewBox="0 0 24 24" aria-hidden="true"><path d="M6.6 10.8a15.1 15.1 0 0 0 6.6 6.6l2.2-2.2c.3-.3.7-.4 1-.2 1.1.4 2.3.6 3.6.6.6 0 1 .4 1 1V20c0 .6-.4 1-1 1A17 17 0 0 1 3 4c0-.6.4-1 1-1h3.5c.6 0 1 .4 1 1 0 1.3.2 2.5.6 3.6.1.3 0 .7-.2 1z"/></svg>
        <span>012345678901</span>
      </li>
      <li>
        <svg viewBox="0 0 24 24" aria-hidden="true"><path d="M2 5h20v14H2z M2 5l10 8 10-8" fill="none" stroke="#222528" stroke-width="2"/></svg>
        <span>mustermann@codewerk.de</span>
      </li>
      <li>
        <svg viewBox="0 0 24 24" aria-hidden="true"><circle cx="12" cy="12" r="10" fill="none" stroke="#222528" stroke-width="2"/><path d="M2 12h20M12 2c3 3 3 17 0 20M12 2c-3 3-3 17 0 20" fill="none" stroke="#222528" stroke-width="1.6"/></svg>
        <span>codewerk-lindner.de</span>
      </li>
    </ul>
  </section>

</body>
</html>
```